Automotive Business Card Design

I would just like a automotive themed card. nothing too extravagant, but catchy.

needs to say something about doing roadside assistance,mobile repairs, Diesel repairs, and Fleet maintenance

it can be single sided or double sided. no preference there.

Industry/Entity Type

Automotive

Contact Information for Business Card

Dean Marwick
phone 519 374 2083
Name: Brightway Automotive & Diesel Repair

```html
<!DOCTYPE html>
<html lang="en">
<head>
<meta charset="utf-8">
<title>Brightway Automotive &amp; Diesel Repair – Business Card</title>
<link rel="stylesheet" href="https://fonts.googleapis.com/css2?family=Michroma&family=Exo+2:wght@400;500&display=swap">
<style>
  :root {
    --backdrop: #e9e6e2;
    --card: #ffffff;
    --card-shade: #eceeef;
    --brand-blue: #1f86d6;
    --deep-blue: #2547b4;
    --bright-blue: #14a6ee;
    --steel: #a9adb2;
    --ink: #2b2f33;
    --muted: #5d6268;
  }
  * { box-sizing: border-box; margin: 0; padding: 0; }
  html, body { width: 1200px; height: 900px; overflow: hidden; }
  body {
    background: var(--backdrop);
    display: flex;
    flex-direction: column;
    align-items: center;
    justify-content: center;
    gap: 60px;
    font-family: "Exo 2", sans-serif;
  }
  .card {
    position: relative;
    width: 600px;
    height: 343px;
    background: radial-gradient(ellipse at 55% 45%, var(--card) 40%, var(--card-shade) 100%);
    box-shadow: 0 10px 28px rgba(0,0,0,.18);
    overflow: hidden;
  }
  .brand {
    display: flex;
    align-items: center;
    gap: 14px;
  }
  .brand-dot {
    width: 46px; height: 46px;
    border-radius: 50%;
    background: var(--brand-blue);
    flex: none;
  }
  .brand-name {
    font-family: "Michroma", sans-serif;
    color: var(--brand-blue);
    font-size: 15px;
    line-height: 1.45;
    letter-spacing: .5px;
    text-transform: uppercase;
  }
  /* front */
  .card-front .brand { position: absolute; left: 34px; top: 34px; }
  .contact {
    position: absolute;
    left: 300px;
    top: 110px;
  }
  .person-name {
    font-family: "Michroma", sans-serif;
    color: var(--brand-blue);
    font-size: 15px;
    letter-spacing: .6px;
    text-transform: uppercase;
  }
  .person-role {
    font-size: 12px;
    color: var(--muted);
    font-style: italic;
    margin-top: 2px;
  }
  .contact-list {
    list-style: none;
    margin-top: 16px;
    display: grid;
    gap: 5px;
  }
  .contact-list li {
    display: flex;
    align-items: center;
    gap: 9px;
    font-size: 12.5px;
    color: var(--ink);
    letter-spacing: .3px;
  }
  .contact-list svg { width: 13px; height: 13px; flex: none; }
  .band {
    position: absolute;
    left: 0; bottom: 0;
    width: 600px; height: 110px;
  }
  .address {
    position: absolute;
    left: 34px;
    bottom: 22px;
    color: #fff;
    font-size: 14px;
    letter-spacing: .6px;
  }
  /* back */
  .card-back {
    display: flex;
    flex-direction: column;
    align-items: center;
    justify-content: center;
    gap: 26px;
  }
  .card-back .brand-dot { width: 58px; height: 58px; }
  .card-back .brand-name { font-size: 17px; }
  .services {
    list-style: none;
    display: flex;
    align-items: center;
    gap: 10px;
    font-size: 12.5px;
    font-weight: 500;
    color: var(--muted);
    letter-spacing: .6px;
    text-transform: uppercase;
  }
  .services li + li::before {
    content: "";
    display: inline-block;
    width: 5px; height: 5px;
    border-radius: 50%;
    background: var(--brand-blue);
    margin-right: 10px;
    vertical-align: middle;
  }
</style>
</head>
<body>

  <section class="card card-front" aria-label="Business card front">
    <div class="brand">
      <span class="brand-dot"></span>
      <p class="brand-name">Brightway Automotive<br>&amp; Diesel Repair</p>
    </div>

    <div class="contact">
      <p class="person-name">Dean Marwick</p>
      <p class="person-role">Managing Director</p>
      <ul class="contact-list">
        <li>
          <svg viewBox="0 0 16 16" aria-hidden="true"><path d="M4 1.5l2.4 3-1.4 1.8c.9 1.9 2.3 3.3 4.2 4.2l1.8-1.4 3 2.4-1.6 2.5C7.3 14 2 8.7 1.5 3.1z" fill="var(--deep-blue)"/></svg>
          519 374 2083
        </li>
        <li>
          <svg viewBox="0 0 16 16" aria-hidden="true"><rect x="4" y="1" width="8" height="14" rx="1.5" fill="none" stroke="var(--deep-blue)" stroke-width="1.6"/><circle cx="8" cy="12.3" r="1" fill="var(--deep-blue)"/></svg>
          519 374 2091
        </li>
        <li>
          <svg viewBox="0 0 16 16" aria-hidden="true"><rect x="1" y="3" width="14" height="10" rx="1" fill="var(--deep-blue)"/><path d="M1.5 3.8L8 9l6.5-5.2" fill="none" stroke="#fff" stroke-width="1.2"/></svg>
          dean@brightwayauto.com
        </li>
        <li>
          <svg viewBox="0 0 16 16" aria-hidden="true"><circle cx="8" cy="8" r="6.5" fill="none" stroke="var(--deep-blue)" stroke-width="1.4"/><ellipse cx="8" cy="8" rx="2.8" ry="6.5" fill="none" stroke="var(--deep-blue)" stroke-width="1.1"/><path d="M1.5 8h13" stroke="var(--deep-blue)" stroke-width="1.1"/></svg>
          www.brightwayauto.com
        </li>
      </ul>
    </div>

    <svg class="band" viewBox="0 0 600 110" preserveAspectRatio="none" aria-hidden="true">
      <defs>
        <linearGradient id="band-fill" x1="0" y1="0" x2="1" y2="0">
          <stop offset="0" stop-color="var(--deep-blue)"/>
          <stop offset=".55" stop-color="var(--bright-blue)"/>
          <stop offset="1" stop-color="var(--deep-blue)"/>
        </linearGradient>
      </defs>
      <path d="M0 36 C180 58 420 58 600 2 L600 110 L0 110 Z" fill="var(--steel)"/>
      <path d="M0 46 C190 66 420 66 600 14 L600 110 L0 110 Z" fill="url(#band-fill)"/>
    </svg>
    <p class="address">214 Harlow Street Unit 3 Kenton</p>
  </section>

  <section class="card card-back" aria-label="Business card back">
    <div class="brand">
      <span class="brand-dot"></span>
      <p class="brand-name">Brightway Automotive<br>&amp; Diesel Repair</p>
    </div>
    <ul class="services" aria-label="Services">
      <li>Roadside Assistance</li>
      <li>Mobile Repairs</li>
      <li>Diesel Repairs</li>
      <li>Fleet Maintenance</li>
    </ul>
  </section>

</body>
</html>
```